Re-design of website: www.velmarpromo.ca/en/

Velmar Promo is a promotional agency specializing in on-site marketing. We are re-designing their website.

We have already produced a prototype:
http://borquelab.com/velmarpromo_siteweb/

The architecture in the prototype must be respected. Please dress up the design with green, grey and black circles and other textures found on their current website www.velmarpromo.ca

Inspiration for design that we like, clean, flat design:

- http://www.tundrafolk.co/
- http://quillborough.com/#!/process
- http://wearedelvani.com/

Delivrables: PSD files of each page of the prototype

Here are the images of their print portfolio: http://ftp.velmarpromo.ca/clients/VMP/VELMARPROMO-PORTFOLIO-2012_EN.zip

Industry/Entity Type

Architecture

Requirements
Must have
• Responsive Design

```html
<!DOCTYPE html>
<html lang="fr">
<head>
<meta charset="utf-8">
<title>Velmar Promo</title>
<link href="https://fonts.googleapis.com/css2?family=Oswald:wght@600;700&family=Source+Sans+3:wght@400;600;700&display=swap" rel="stylesheet">
<style>
:root{
  --green:#6cb33f;
  --green-light:#8cc63f;
  --green-dark:#5a9e33;
  --ink:#222;
  --white:#fff;
  --band:#e6e7e8;
  --caption:rgba(40,40,40,.72);
  --dark-circle:#3a3a3a;
}
*{margin:0;padding:0;box-sizing:border-box}
html,body{width:956px;height:1200px;overflow:hidden;background:var(--white)}
body{position:relative;font-family:"Source Sans 3",Arial,sans-serif;color:var(--ink)}

.site-header{position:absolute;left:0;top:0;width:956px;height:70px}
.brand{position:absolute;left:0;width:956px;top:18px;display:flex;justify-content:center;align-items:center;gap:10px}
.brand-name{font-weight:700;font-size:30px;letter-spacing:4px;color:#1d1d1d}
.brand-dot{width:40px;height:40px;border-radius:50%;background:var(--green-light)}
.lang-switch{position:absolute;left:786px;top:5px;width:46px;height:20px;border:1px solid #c8c8c8;border-radius:2px;background:linear-gradient(#fff,#ececec);font-size:9px;color:#333;display:flex;align-items:center;justify-content:center;box-shadow:0 1px 1px rgba(0,0,0,.15)}

.main-nav{position:absolute;left:0;top:70px;width:956px;height:28px;background:linear-gradient(#9dcf55,var(--green) 55%,#79b83c)}
.main-nav a{position:absolute;top:0;height:28px;line-height:28px;font-size:11px;font-weight:600;color:var(--white);text-decoration:none;text-shadow:0 1px 1px rgba(0,0,0,.25)}
.nav-divider{position:absolute;top:0;width:1px;height:28px;background:rgba(255,255,255,.55)}
.social{position:absolute;left:750px;top:7px;display:flex;gap:4px}
.social span{width:16px;height:16px;border-radius:3px;background:#5d8fb0}
.social span:nth-child(2){background:#5bb5de}
.social span:nth-child(3){background:#2f77ac}
.social span:nth-child(4){background:#c0392b}

.hero{position:absolute;left:122px;top:102px;width:713px;height:346px;background:var(--green);overflow:hidden}
.hero-visual{position:absolute;right:0;top:0;width:420px;height:346px;background:radial-gradient(ellipse at 60% 55%,#f0a81a 0%,#c9a92a 18%,#86be44 45%,var(--green) 80%)}
.hero-title{position:absolute;left:30px;top:64px;font-family:"Oswald",Impact,sans-serif;font-weight:700;font-size:25px;line-height:36px;color:var(--white);text-transform:uppercase;letter-spacing:-.2px}
.hero-btn{position:absolute;left:32px;top:180px;width:82px;height:31px;background:linear-gradient(#3a3a3a,#151515);border-radius:2px;font-family:"Oswald",Impact,sans-serif;font-weight:600;font-size:13px;color:var(--green-light);display:flex;align-items:center;justify-content:center}
.hero-dots{position:absolute;left:36px;top:290px;display:flex;gap:5px}
.hero-dots span{width:12px;height:12px;border-radius:50%;background:var(--white)}
.hero-dots span.active{background:radial-gradient(circle,#222 0 2.5px,var(--white) 3px)}
.arrow{position:absolute;top:258px;width:34px;height:34px}

.section-title{position:absolute;left:0;width:956px;top:464px;text-align:center;font-size:19px;font-weight:400;letter-spacing:.3px;color:#222}

.work{position:absolute;width:349px;height:189px;border:1px solid #d0d0d0;overflow:hidden}
.work-caption{position:absolute;left:0;bottom:0;width:100%;height:32px;background:var(--caption);color:var(--white);font-size:11.5px;font-weight:600;line-height:32px;padding-left:12px;text-transform:uppercase}

.info-band{position:absolute;left:0;top:908px;width:956px;height:254px;background:var(--band)}
.feature{position:absolute;top:18px;width:220px;text-align:center}
.feature-circle{position:relative;width:174px;height:174px;margin:0 auto;border-radius:50%;border:2px solid #9a9a9a;overflow:hidden}
.feature-label{position:absolute;left:0;bottom:0;width:100%;height:66px;background:rgba(60,60,60,.35);border-radius:50% 50% 0 0/40% 40% 0 0;color:var(--white);font-size:17px;padding-top:14px}
.feature-text{margin-top:8px;font-size:10.5px;line-height:15px;color:#333}

.site-footer{position:absolute;left:0;top:1174px;width:956px;text-align:center;font-size:9.5px;color:#333}
</style>
</head>
<body>
<header class="site-header">
  <div class="brand"><span class="brand-name">VELMAR PROMO</span><span class="brand-dot"></span></div>
  <div class="lang-switch">English</div>
</header>

<nav class="main-nav">
  <a style="left:137px">AGENCE</a><span class="nav-divider" style="left:189px"></span>
  <a style="left:204px">SERVICES</a><span class="nav-divider" style="left:260px"></span>
  <a style="left:273px">REALISATIONS</a><span class="nav-divider" style="left:354px"></span>
  <a style="left:367px">EVENEMENTS</a><span class="nav-divider" style="left:447px"></span>
  <a style="left:463px">RECRUTEMENT</a><span class="nav-divider" style="left:549px"></span>
  <a style="left:566px">CONTACT</a>
  <div class="social"><span></span><span></span><span></span><span></span></div>
</nav>

<section class="hero">
  <div class="hero-visual" role="img" aria-label="Bouteille de bière légère éclaboussée d'eau sur fond vert"></div>
  <h1 class="hero-title">Lorem ipsum is simply<br>dummy text of the printing<br>and typesetting industry.</h1>
  <div class="hero-btn">READ MORE</div>
  <div class="hero-dots"><span></span><span class="active"></span><span></span><span></span></div>
</section>
<svg class="arrow" style="left:84px" viewBox="0 0 34 34"><circle cx="17" cy="17" r="17" fill="#1a1a1a"/><path d="M20 10l-7 7 7 7" fill="none" stroke="#fff" stroke-width="3.5" stroke-linecap="round" stroke-linejoin="round"/></svg>
<svg class="arrow" style="left:837px" viewBox="0 0 34 34"><circle cx="17" cy="17" r="17" fill="#1a1a1a"/><path d="M14 10l7 7-7 7" fill="none" stroke="#fff" stroke-width="3.5" stroke-linecap="round" stroke-linejoin="round"/></svg>

<h2 class="section-title">NOS RÉALISATIONS 360</h2>

<article class="work" style="left:122px;top:502px" role="img" aria-label="Fruits tranchés et éclaboussure de lait">
  <div style="position:absolute;inset:0;background:linear-gradient(110deg,#f4f4f4 30%,#f2c13a 60%,#e0402f 85%,#f0a020)"></div>
  <div class="work-caption">Lorem ipsum is simply dummy tex</div>
</article>
<article class="work" style="left:486px;top:502px" role="img" aria-label="Deux promotrices en tuques lors d'un événement hivernal">
  <div style="position:absolute;inset:0;background:linear-gradient(120deg,#8a7a62,#3a2e28 50%,#2a2624 75%,#cfcfcf)"></div>
  <div class="work-caption">Lorem ipsum is simply dummy tex</div>
</article>
<article class="work" style="left:122px;top:705px" role="img" aria-label="Verre de bière ambrée avec étiquette">
  <div style="position:absolute;inset:0;background:linear-gradient(100deg,#c98850,#8a4a1e 45%,#6b3410)"></div>
  <div class="work-caption">Lorem ipsum is simply dummy tex</div>
</article>
<article class="work" style="left:486px;top:705px" role="img" aria-label="Équipe de promotion en vestes vertes devant un kiosque">
  <div style="position:absolute;inset:0;background:linear-gradient(180deg,#5a4a3a 0%,#3e8a3a 40%,#e8e8e0 75%,#b9cf3e)"></div>
  <div class="work-caption">Lorem ipsum is simply dummy tex</div>
</article>

<section class="info-band">
  <div class="feature" style="left:139px">
    <div class="feature-circle" role="img" aria-label="Agente du service client avec casque d'écoute" style="background:linear-gradient(135deg,#b8673a,#e9c9a8 50%,#f2f2f2)">
      <div class="feature-label">CONTACT</div>
    </div>
    <p class="feature-text">Lorem Ipsum is simply dummy text of the<br>printing and typesetting industry</p>
  </div>
  <div class="feature" style="left:373px">
    <div class="feature-circle" role="img" aria-label="Globe bleu entouré de silhouettes se tenant la main" style="background:radial-gradient(circle at 40% 40%,#a8c0dc,#4e6f9c 70%,#2e4a72)">
      <div class="feature-label">RECRUITMENT</div>
    </div>
    <p class="feature-text">Lorem Ipsum is simply dummy text of the<br>printing and typesetting industry</p>
  </div>
  <div class="feature" style="left:600px">
    <div class="feature-circle" style="background:var(--dark-circle)">
      <svg style="position:absolute;left:63px;top:30px" width="44" height="48" viewBox="0 0 44 48"><circle cx="22" cy="12" r="11" fill="#fff"/><path d="M2 46v-8c0-8 6-13 14-13h12c8 0 14 5 14 13v8z" fill="#fff"/><path d="M19 26h6l-1 4 2 14h-8l2-14z" fill="#3a3a3a"/></svg>
      <div class="feature-label" style="background:rgba(25,25,25,.55)">FOLLOW US</div>
    </div>
    <p class="feature-text">Lorem Ipsum is simply dummy text of the<br>printing and typesetting industry</p>
  </div>
</section>

<footer class="site-footer">(C) VELMAR PROMO. TOUS DROITS RÉSERVÉS</footer>
</body>
</html>
```